RTW Business Card Design

We are an independent auto dealer who specializes in commercial & fleet vehicles, we are family owned and operated and have been in business since 2001. We stock late model, low mileage, white trucks & vans. We mostly deal with companies in the construction and service industries. We are just looking to try to freshen up our old business card, we do not want to change the logo at this point, because it is well know within the southwest region & construction community. I have attached our logo and a PDF of our current business card for reference.
Updates
If the address is stacked there is no comma (,) after NE. Everyone keeps putting it in with this format and it is not correct.
842 Ventana Blvd NE
Albuquerque, NM 87120
If the address is all on one line, then there will be a comma (,) after NE
842 Ventana Blvd NE, Albuquerque, NM 87120
Please make changes accordingly, thank you for your attention in this matter.
Industry/Entity Type
Construction
Contact Information for Business Card
842 Ventana Blvd NE, Albuquerque, NM 87120, Marcus Delaney, Vice President, marcus@rtwvehicledepot.com, www.RTWvehicledepot.com, ph 505-610-2247, fax 505-472-8156, cell 505-238-6094
Look and feel
Each slider illustrates characteristics of the customer's brand and the style your logo design should communicate.

```html
<!DOCTYPE html>
<html lang="en">
<head>
<meta charset="utf-8">
<title>RTW Auto Sales – Business Card</title>
<link rel="stylesheet" href="https://fonts.googleapis.com/css2?family=Open+Sans:wght@400;600;700&display=swap">
<style>
  :root {
    --backdrop: #e6e4e1;
    --card-white: #ffffff;
    --band-black: #111111;
    --accent-red: #e0212b;
    --ink-dark: #1a1a1a;
    --ink-grey: #6a6a6a;
    --ink-light: #f2f2f2;
  }
  * { margin: 0; padding: 0; box-sizing: border-box; }
  html, body { width: 1200px; height: 800px; overflow: hidden; }
  body {
    background: var(--backdrop);
    font-family: "Open Sans", Arial, sans-serif;
    position: relative;
  }
  .business-card {
    position: absolute;
    left: 180px; top: 160px;
    width: 840px; height: 480px;
    background: var(--card-white);
    overflow: hidden;
    box-shadow: 0 10px 30px rgba(0,0,0,0.18);
  }
  .card-graphics { position: absolute; inset: 0; }
  .brand {
    position: absolute;
    left: 150px; top: 50px;
    display: flex; align-items: flex-end; gap: 22px;
  }
  .brand-name {
    font-size: 50px; font-weight: 700;
    color: var(--ink-dark);
    line-height: 1;
    letter-spacing: -0.5px;
  }
  .brand-tagline {
    font-size: 13px; color: var(--ink-grey);
    line-height: 1.35;
    padding-bottom: 4px;
  }
  .contact-list {
    position: absolute;
    left: 36px; top: 252px;
    list-style: none;
  }
  .contact-list li {
    display: flex; align-items: center; gap: 12px;
    height: 28px;
    color: var(--ink-light);
    font-size: 18px;
  }
  .contact-icon { width: 20px; height: 20px; flex: none; }
  .office {
    position: absolute;
    left: 370px; top: 366px;
    color: var(--ink-light);
    font-size: 18px; line-height: 25px;
  }
  .office-name { color: var(--accent-red); font-weight: 700; }
  .person {
    position: absolute;
    right: 42px; top: 196px;
    text-align: right;
  }
  .person-name {
    color: var(--accent-red);
    font-size: 28px; font-weight: 700; line-height: 1.2;
  }
  .person-title {
    color: var(--ink-dark);
    font-size: 17px; line-height: 1.5;
  }
</style>
</head>
<body>
  <div class="business-card">
    <svg class="card-graphics" width="840" height="480" viewBox="0 0 840 480" aria-hidden="true">
      <polygon points="0,150 840,380 840,480 0,480" fill="var(--band-black)"/>
      <line x1="0" y1="128" x2="840" y2="358" stroke="var(--accent-red)" stroke-width="4"/>
      <line x1="0" y1="139" x2="840" y2="369" stroke="var(--accent-red)" stroke-width="3"/>
    </svg>

    <div class="brand">
      <span class="brand-name">RTW Auto Sales</span>
      <span class="brand-tagline">Specializing in Commercial<br>&amp; Fleet Vehicles</span>
    </div>

    <ul class="contact-list">
      <li>
        <svg class="contact-icon" viewBox="0 0 20 20"><rect width="20" height="20" rx="4" fill="var(--accent-red)"/><path d="M6 4.5c1 0 1.5 2.2 1.2 3L6.4 8.3c.8 1.6 2 2.9 3.4 3.6l.8-.8c.8-.3 3 .2 3 1.2v1.6c0 .8-.8 1.4-1.6 1.2C8 14.3 5.4 11.8 4.6 7.9 4.4 7 5 4.5 6 4.5z" fill="#fff"/></svg>
        <span>505-610-2247</span>
      </li>
      <li>
        <svg class="contact-icon" viewBox="0 0 20 20"><rect width="20" height="20" rx="4" fill="var(--accent-red)"/><rect x="5" y="4" width="8" height="5" fill="#fff"/><rect x="4" y="9" width="12" height="7" rx="1" fill="#fff"/><rect x="6" y="11" width="6" height="1.5" fill="var(--accent-red)"/></svg>
        <span>505-472-8156</span>
      </li>
      <li>
        <svg class="contact-icon" viewBox="0 0 20 20"><rect width="20" height="20" rx="4" fill="var(--accent-red)"/><rect x="6.5" y="3.5" width="7" height="13" rx="1.5" fill="#fff"/><rect x="8" y="5.5" width="4" height="7" fill="var(--accent-red)"/></svg>
        <span>505-238-6094</span>
      </li>
      <li>
        <svg class="contact-icon" viewBox="0 0 20 20"><rect width="20" height="20" rx="4" fill="var(--accent-red)"/><rect x="4" y="6" width="12" height="8.5" rx="1" fill="#fff"/><path d="M4.5 6.5 10 11l5.5-4.5" stroke="var(--accent-red)" stroke-width="1.3" fill="none"/></svg>
        <span>marcus@rtwvehicledepot.com</span>
      </li>
    </ul>

    <div class="office">
      <div class="office-name">RTW Auto Sales</div>
      <div>842 Ventana Blvd NE</div>
      <div>Albuquerque, NM 87120</div>
      <div>www.RTWvehicledepot.com</div>
    </div>

    <div class="person">
      <div class="person-name">Marcus Delaney</div>
      <div class="person-title">Vice President</div>
    </div>
  </div>
</body>
</html>
```